Figure for presentation on a hybrid research project

We need a figure that shows a series of 6 technical projects feeding into 3 multidisciplinary hybrid projects.
The concept is a ring of 6 technical projects, which could look like a 6 colour swirl (see
https://en.quorbelpedia.org/wiki/Path_artwork for an example of a 4 colour swirl.)
The 3 hybrid projects sit in the centre because they rely on input from many of the surrounding technical projects.
I've drawn a rough version in Powerpoint - see attached file uploaded. Note, in my example I couldn't draw the swirling outer ring and the colour selection is poor. The acronym for the overall Centre using the figure is CryoLUX, so we will have a mint leaf and turquoise green in the logo, plus also nerves, since we will be researching neural interconnections.
We ABSOLUTELY NEED the final form of the figure to include vector graphics formats (including a form that can be edited in Photoshop) because we may need to change the title of the technical projects or of the hybrid projects at short notice ourselves.

Target Market(s)

Academic: eminent scientists and engineers

Industry/Entity Type

Technical

Font styles to use
Sans Serif

Colors
04a990

Requirements
Must have
• The projects around the ring with all project titles legible; the final figure will be reduced to no more than 8cm x 8cm in the proposal (probably less).
• Only one colour selected, because we have included that colour in the logo that we are having designed. Otherwise, a colour series around the ring that is pleasant, and another compatible colour series for the inter 3 projects.
• We ABSOLUTELY NEED the final form of the figure to include vector graphics formats (including a form that can be edited in Photoshop) because we may need to change the title of the technical projects or of the hybrid projects at short notice ourselves.
Nice to have
• See the figure we uploaded; that's the essence
• HOWEVER VIP: two of the titles around the outer ring have changed slightly.
• Computational Modelling is now Neuronal Modelling and
• Signal Processing is now Non-Invasive Interfaces (note that I've now changed the titles on the uploaded figure)

```html
<!DOCTYPE html>
<html lang="en">
<head>
<meta charset="utf-8">
<title>Research Programme Structure</title>
<link rel="stylesheet" href="https://fonts.googleapis.com/css2?family=Outfit:wght@400;700&display=swap">
<style>
  :root {
    --teal: #04a990;
    --teal-light: #07a68d;
    --teal-mid: #05967d;
    --teal-deep: #047a5f;
    --teal-dark: #05745a;
    --paper: #ffffff;
    --label: #ffffff;
  }
  html, body {
    margin: 0;
    padding: 0;
    width: 1200px;
    height: 999px;
    overflow: hidden;
    background: var(--paper);
  }
  .canvas {
    position: relative;
    width: 1200px;
    height: 999px;
    background: var(--paper);
  }
  .programme-figure {
    display: block;
    width: 1200px;
    height: 999px;
  }
  .segment {
    stroke: var(--paper);
    stroke-width: 8;
    stroke-linejoin: round;
  }
  .segment--gene { fill: var(--teal-light); }
  .segment--electro { fill: var(--teal-deep); }
  .segment--optrode { fill: var(--teal-mid); }
  .segment--neuronal { fill: var(--teal-dark); }
  .segment--noninvasive { fill: var(--teal-light); }
  .segment--living { fill: var(--teal-deep); }
  .project-label {
    font-family: "Outfit", sans-serif;
    font-weight: 400;
    font-size: 24px;
    letter-spacing: 0.3px;
    fill: var(--label);
  }
  .hub {
    fill: var(--paper);
    stroke: var(--teal);
    stroke-width: 4;
  }
  .hub-divider {
    stroke: var(--teal);
    stroke-width: 3.5;
    stroke-linecap: round;
  }
  .hybrid-label {
    font-family: "Outfit", sans-serif;
    font-weight: 700;
    font-size: 23px;
    letter-spacing: 0.3px;
    fill: var(--teal);
    text-anchor: middle;
  }
</style>
</head>
<body>
<main class="canvas">
  <svg class="programme-figure" viewBox="0 0 1200 999" xmlns="http://www.w3.org/2000/svg"
       role="img" aria-label="Six technical projects in a ring around three hybrid projects">
    <defs>
      <path id="track-gene" d="M 565.1 173.2 A 320 320 0 0 1 855.1 308.4"/>
      <path id="track-living" d="M 303.0 356.8 A 320 320 0 0 1 565.1 173.2"/>
      <path id="track-noninvasive" d="M 330.9 675.6 A 320 320 0 0 1 303.0 356.8"/>
      <path id="track-electro" d="M 899.3 634.8 A 338 338 0 0 0 869.9 298.1"/>
      <path id="track-optrode" d="M 622.5 828.7 A 338 338 0 0 0 899.3 634.8"/>
      <path id="track-neuronal" d="M 316.1 685.9 A 338 338 0 0 0 622.5 828.7"/>
    </defs>

    <g class="technical-ring">
      <path class="segment segment--gene" d="M 556.4 73.6 A 420 420 0 0 1 937.1 251.1 L 788.0 355.5 A 238 238 0 0 0 572.2 254.9 Z"/>
      <path class="segment segment--electro" d="M 937.1 251.1 A 420 420 0 0 1 973.6 669.5 L 808.7 592.6 A 238 238 0 0 0 788.0 355.5 Z"/>
      <path class="segment segment--optrode" d="M 973.6 669.5 A 420 420 0 0 1 629.6 910.4 L 613.8 729.1 A 238 238 0 0 0 808.7 592.6 Z"/>
      <path class="segment segment--neuronal" d="M 629.6 910.4 A 420 420 0 0 1 248.9 732.9 L 398.0 628.5 A 238 238 0 0 0 613.8 729.1 Z"/>
      <path class="segment segment--noninvasive" d="M 248.9 732.9 A 420 420 0 0 1 212.4 314.5 L 377.3 391.4 A 238 238 0 0 0 398.0 628.5 Z"/>
      <path class="segment segment--living" d="M 212.4 314.5 A 420 420 0 0 1 556.4 73.6 L 572.2 254.9 A 238 238 0 0 0 377.3 391.4 Z"/>
    </g>

    <g class="technical-labels">
      <text class="project-label"><textPath href="#track-gene" startOffset="50%" text-anchor="middle">Gene-regulated Interfaces</textPath></text>
      <text class="project-label"><textPath href="#track-electro" startOffset="50%" text-anchor="middle">Electro-modulated Interfaces</textPath></text>
      <text class="project-label"><textPath href="#track-optrode" startOffset="50%" text-anchor="middle">Optrode Interfaces</textPath></text>
      <text class="project-label"><textPath href="#track-neuronal" startOffset="50%" text-anchor="middle">Neuronal Modelling</textPath></text>
      <text class="project-label"><textPath href="#track-noninvasive" startOffset="50%" text-anchor="middle">Non-invasive Interfaces</textPath></text>
      <text class="project-label"><textPath href="#track-living" startOffset="50%" text-anchor="middle">Living Electrodes</textPath></text>
    </g>

    <g class="hybrid-hub">
      <circle class="hub" cx="593" cy="492" r="224"/>
      <line class="hub-divider" x1="593" y1="492" x2="704" y2="299.7"/>
      <line class="hub-divider" x1="593" y1="492" x2="668.9" y2="700.6"/>
      <line class="hub-divider" x1="593" y1="492" x2="374.4" y2="530.5"/>
      <text class="hybrid-label" x="560" y="398">CONNECTION</text>
      <text class="hybrid-label" x="487" y="574">PERCEPTION</text>
      <text class="hybrid-label" x="712" y="528">INTERACTION</text>
    </g>
  </svg>
</main>
</body>
</html>
```